TKA Electricial Contracting Services

Hi guys, after a design for my small electrical company, have logo design files to be incorporated into the layout, the basic concept is electrical contracting services for residential, commercial, industrial & data services, image is clean clear and strong,

Card format is to have a nice clean logo on front,with maybe the Residential – commercial – industrial - data, followed with licensed & insured, followed by contact details on backside of the card.

Target Market(s)

Residential, commercial, industrial sectors.

Industry/Entity Type

Electrical

Contact Information for Business Card

TKA logo,
Residential – commercial – industrial - data
REC: 61372
Email: tka@poralink.net.au
Phone: 0458 203 719

Requirements
Must have
• Clean & strong design.
Nice to have
• If possible, I would like the logo colours inverted so the text is orange and the background is black on the front of the card, then the backside of the card be the reverse colour
Should not have
• No Sparks, lightning bolts,

```html
<!DOCTYPE html>
<html lang="en">
<head>
<meta charset="utf-8">
<title>TKA Electrical – Business Card</title>
<link href="https://fonts.googleapis.com/css2?family=Urbanist:wght@400;700;800&display=swap" rel="stylesheet">
<style>
  :root {
    --backdrop: #e9e4de;
    --card-orange: #f5832d;
    --card-edge: #8a8a8a;
    --ink: #111111;
  }
  * { margin: 0; padding: 0; box-sizing: border-box; }
  html, body {
    width: 1200px;
    height: 750px;
    overflow: hidden;
    background: var(--backdrop);
    font-family: "Urbanist", sans-serif;
    color: var(--ink);
  }
  .canvas {
    position: relative;
    width: 1200px;
    height: 750px;
  }
  .card {
    position: absolute;
    top: 238px;
    width: 490px;
    height: 281px;
    background: var(--card-orange);
    border: 2px solid var(--card-edge);
  }
  .card--front { left: 90px; }
  .card--back  { left: 623px; }

  /* Front */
  .brand-name {
    position: absolute;
    left: 0;
    right: 0;
    top: 48px;
    text-align: center;
    font-weight: 800;
    font-size: 98px;
    line-height: 1;
    letter-spacing: -2px;
  }
  .business-name {
    position: absolute;
    left: 140px;
    top: 146px;
    font-weight: 700;
    font-size: 19px;
    letter-spacing: 0.3px;
  }
  .services {
    position: absolute;
    left: 0;
    right: 0;
    top: 174px;
    text-align: center;
    font-weight: 400;
    font-size: 17px;
    line-height: 21px;
  }

  /* Back */
  .contact-name {
    position: absolute;
    left: 0;
    right: 0;
    top: 93px;
    text-align: center;
    font-weight: 700;
    font-size: 22px;
  }
  .contact-list {
    position: absolute;
    left: 133px;
    top: 142px;
    list-style: none;
    font-size: 18px;
    line-height: 22px;
  }
  .contact-list .label { display: inline-block; width: 68px; }
</style>
</head>
<body>
  <main class="canvas">
    <section class="card card--front" aria-label="Card front">
      <div class="brand-name">TKA</div>
      <div class="business-name">Tom Kendall Electrical</div>
      <p class="services">Residential – commercial – industrial<br>data REC: 61372</p>
    </section>

    <section class="card card--back" aria-label="Card back">
      <h1 class="contact-name">Tom Kendall</h1>
      <ul class="contact-list">
        <li><span class="label">Email:</span>tka@poralink.net.au</li>
        <li>Phone: 0458 203 719</li>
      </ul>
    </section>
  </main>
</body>
</html>
```